Brochure for a high tech company
Design brochure for products including - Solar Panels, Solar inverter, Electronic Bidet, LED Bulb
Our customers are corporate , hotels , offices and retail customers.

```html
<!DOCTYPE html>
<html lang="en">
<head>
<meta charset="utf-8">
<title>Lumora Product Brochure</title>
<link rel="stylesheet" href="https://fonts.googleapis.com/css2?family=Montserrat:wght@600;700&family=Open+Sans:wght@400;600&display=swap">
<style>
  :root{
    --bg:#d9d9d9;
    --paper:#ffffff;
    --ink:#111111;
    --body:#3a3a3a;
    --muted:#8a8a8a;
    --black:#0b0b0b;
    --panel-blue:#2a4f9c;
    --skin-a:#8a5a45;
    --skin-b:#2a1a16;
    --light:#e9eef2;
  }
  *{margin:0;padding:0;box-sizing:border-box}
  html,body{width:1200px;height:901px;overflow:hidden}
  body{background:var(--bg);font-family:"Open Sans",Arial,sans-serif;color:var(--body);position:relative}

  .brand{display:flex;align-items:center;gap:8px;font-family:"Montserrat",Arial,sans-serif;font-weight:700;letter-spacing:.5px}
  .brand__dot{width:22px;height:22px;border-radius:50%;border:2px solid currentColor;flex:none}
  .brand__name{font-size:22px}
  .brand__tag{font-size:7px;font-family:"Open Sans",sans-serif;font-weight:400;color:var(--muted)}

  /* Cover */
  .cover{position:absolute;left:360px;top:36px;width:480px;height:350px;background:var(--black);color:#fff;overflow:hidden;box-shadow:0 6px 18px rgba(0,0,0,.25)}
  .cover__portrait{position:absolute;left:0;top:60px;width:190px;height:290px;background:radial-gradient(ellipse at 45% 40%,var(--skin-a),var(--skin-b) 70%,var(--black))}
  .cover__bulb{position:absolute;left:200px;top:62px;width:62px;height:62px;border-radius:50%;background:radial-gradient(circle at 40% 35%,#ffffff,#c9d3dc 70%)}
  .cover__panel{position:absolute;left:255px;top:160px;width:62px;height:92px;background:linear-gradient(135deg,#3c66b8,#1d3a7a)}
  .cover__bidet{position:absolute;left:390px;top:225px;width:66px;height:72px;border-radius:33px 33px 12px 12px;background:radial-gradient(circle at 45% 40%,#ffffff,#cfd4d8 75%)}
  .cover .brand{position:absolute;right:26px;top:16px;color:#fff}
  .cover .brand--big{top:78px;right:26px}
  .cover .brand--big .brand__name{font-size:34px}
  .cover .brand--big .brand__dot{width:36px;height:36px;border-width:3px}
  .cover__url{position:absolute;right:26px;bottom:20px;font-size:9px;color:#cfcfcf}

  /* Inside spread */
  .spread{position:absolute;left:100px;top:440px;width:1000px;height:380px;display:flex;box-shadow:0 8px 22px rgba(0,0,0,.25)}
  .page{position:relative;width:500px;height:380px;background:var(--paper);overflow:hidden}
  .page--left{border-right:1px solid #e2e2e2}

  .about__band{position:absolute;left:0;top:0;width:500px;height:380px}
  .about__portrait{position:absolute;left:0;top:90px;width:230px;height:210px;background:radial-gradient(ellipse at 50% 45%,var(--skin-a),var(--skin-b) 75%)}
  .about__brand{position:absolute;left:140px;top:24px;color:var(--ink)}
  .about__brand .brand__tag{display:block;margin:2px 0 0 30px}
  .about__text{position:absolute;left:262px;top:120px;width:210px;font-size:7.5px;line-height:1.55}
  .about__title{font-family:"Montserrat",sans-serif;font-weight:700;font-size:10px;color:var(--ink);margin-bottom:6px}
  .about__text p{margin-bottom:8px;text-align:justify}
  .about__address{position:absolute;left:30px;bottom:28px;width:180px;font-size:7px;line-height:1.5;color:var(--body);font-style:normal}

  .solar__title{position:absolute;left:28px;top:42px;font-family:"Montserrat",sans-serif;font-weight:700;font-size:17px;color:var(--ink);letter-spacing:.5px}
  .solar__sub{position:absolute;left:28px;top:66px;font-size:7px;color:var(--body)}
  .solar__specs{position:absolute;left:28px;top:96px;width:150px;font-size:7px;line-height:1.8;list-style:none}
  .solar__specs li:first-child{font-weight:600;color:var(--ink)}
  .solar__image{position:absolute;left:176px;top:120px;width:110px;height:160px;background:linear-gradient(135deg,#3e6ac0,var(--panel-blue) 55%,#16306a)}
  .solar__box{position:absolute;left:310px;top:70px;width:170px;height:230px;background:var(--black);color:#e8e8e8;padding:14px}
  .solar__box .brand{color:#fff;justify-content:flex-end}
  .solar__box .brand__name{font-size:16px}
  .solar__box .brand__dot{width:16px;height:16px}
  .solar__box-head{font-size:7px;font-weight:600;margin-top:14px}
  .solar__box-sub{font-size:6.5px;color:#bdbdbd;margin-bottom:10px}
  .solar__box ul{list-style:none;font-size:6.5px;line-height:1.9}
  .solar__box li:first-child{font-weight:600}
  .solar__footer{position:absolute;left:28px;right:28px;bottom:40px;font-size:6.5px;color:var(--body);border-top:1px solid #cccccc;padding-top:6px}
</style>
</head>
<body>

<section class="cover">
  <div class="cover__portrait" role="img" aria-label="Portrait photo of a smiling woman presenting products"></div>
  <div class="cover__bulb" role="img" aria-label="LED bulb product photo"></div>
  <div class="cover__panel" role="img" aria-label="Solar panel product photo"></div>
  <div class="cover__bidet" role="img" aria-label="Electronic bidet product photo"></div>
  <div class="brand"><span class="brand__dot"></span><span class="brand__name">Lumora</span></div>
  <div class="brand brand--big"><span class="brand__dot"></span><span class="brand__name">Lumora</span></div>
  <div class="cover__url">www.lumora-energy.example</div>
</section>

<section class="spread">
  <article class="page page--left">
    <svg class="about__band" viewBox="0 0 500 380" aria-hidden="true">
      <polygon points="0,0 120,0 0,90" fill="#0b0b0b"/>
      <rect x="0" y="90" width="230" height="210" fill="#0b0b0b"/>
    </svg>
    <div class="about__portrait" role="img" aria-label="Photo of a woman in a red sari gesturing toward the text"></div>
    <div class="about__brand">
      <div class="brand"><span class="brand__dot"></span><span class="brand__name">Lumora</span></div>
      <span class="brand__tag">powering ideas</span>
    </div>
    <div class="about__text">
      <h2 class="about__title">About Us</h2>
      <p>Lumora builds clean energy and smart home products for offices, hotels, retail stores and homes. Our solar panels, inverters, LED lighting and bidets are tested for long life and low running cost.</p>
      <p>We work with partners across the region to plan, supply and service every installation.</p>
    </div>
    <address class="about__address">Lumora Energy Pvt Ltd<br>14 Harbour Road, Kestrel Park, 400 210</address>
  </article>

  <article class="page page--right">
    <h1 class="solar__title">SOLAR PV PANELS</h1>
    <p class="solar__sub">Poly Crystalline Module 250W / Tested for harsh climates</p>
    <ul class="solar__specs">
      <li>Key Features</li>
      <li>Max Power: 250 W</li>
      <li>Voltage: 30.5 V</li>
      <li>Current: 8.2 A</li>
      <li>Open Circuit: 37.4 V</li>
      <li>Short Circuit: 8.7 A</li>
      <li>Efficiency: 15.4 %</li>
      <li>Weight: 18.5 kg</li>
    </ul>
    <div class="solar__image" role="img" aria-label="Poly crystalline solar panel photo"></div>
    <div class="solar__box">
      <div class="brand"><span class="brand__dot"></span><span class="brand__name">Lumora</span></div>
      <p class="solar__box-head">Mono Crystalline Module 300W</p>
      <p class="solar__box-sub">Higher output for limited roof space</p>
      <ul>
        <li>Key Features</li>
        <li>Max Power: 300 W</li>
        <li>Efficiency: 18.1 %</li>
        <li>Warranty: 25 years</li>
        <li>Frame: anodised aluminium</li>
      </ul>
    </div>
    <p class="solar__footer">Solar Accessories: mounting frames, cables, junction boxes, charge controllers and battery banks are also available.</p>
  </article>
</section>

</body>
</html>
```